Bright Dabs - Face Painting Company requires business card design

Hi,
I am wanting a business card design for a new business in Brisbane (Australia) called 'Bright Dabs'. We are a childrens face painting company.

I want to communicate a corporate, simple and clean message through my business card, but also fun and relevant to children.

My company colours are black, yellow and purple, and at the moment I am running with a "cheeky smile" type theme, along the lines of the Marchwood Fox (Tobin in Farrowvale).

I want this to look Corporate, clean and simple. On the back I would like to see some creative flair with a border or background design, perhaps in white or another colour.

Requirements
Must have
• Front:
Bright Dabs
Face Painting Designs

Back:
Maren Lockwell
Artist
0491 283 516
maren@brightdabs.com.au
www.brightdabs.com.au
Nice to have
• Attached is the banner which i had made, the business card should go along with this type of theme.
I would like to use the colours Yellow, Black and Purple. Purple should be used in a miniml way, with yellow and black as the main colours.
I want it to have a CORPORATE look.

A Playfull but readable text.

I would like a mix up of the colours on the back in the text.
Maren Lockwell (black)
Artist(purple) etc.

```html
<!DOCTYPE html>
<html lang="en">
<head>
<meta charset="utf-8">
<title>Bright Dabs – Business Card</title>
<link rel="stylesheet" href="https://fonts.googleapis.com/css2?family=Indie+Flower&family=Nunito:wght@400;800&display=swap">
<style>
  :root {
    --slate: #676164;
    --slate-light: #9b9699;
    --sunshine: #f6e83a;
    --tagline: #c7c07a;
    --paper: #ecebe8;
    --white: #ffffff;
    --card-w: 620px;
    --card-h: 378px;
  }
  * { box-sizing: border-box; margin: 0; padding: 0; }
  html, body {
    width: 1200px;
    height: 900px;
    overflow: hidden;
    background: var(--paper);
  }
  .canvas {
    position: relative;
    width: 1200px;
    height: 900px;
  }
  .card {
    position: absolute;
    width: var(--card-w);
    height: var(--card-h);
    overflow: hidden;
    box-shadow: 0 4px 14px rgba(0,0,0,0.18);
  }
  .card__bg {
    position: absolute;
    inset: 0;
    width: 100%;
    height: 100%;
  }
  .card--front { left: 60px; top: 70px; background: var(--sunshine); }
  .card--back  { left: 520px; top: 452px; background: var(--slate); }

  /* Front */
  .brand-mark {
    position: absolute;
    left: 96px;
    top: 120px;
    width: 80px;
    height: 80px;
    border-radius: 50%;
    background: var(--white);
    border: 4px solid var(--slate);
  }
  .brand-name {
    position: absolute;
    font-family: "Nunito", sans-serif;
    font-weight: 800;
    color: var(--slate);
    white-space: nowrap;
    line-height: 1;
  }
  .card--front .brand-name {
    left: 192px;
    top: 126px;
    font-size: 60px;
  }
  .tagline {
    position: absolute;
    font-family: "Indie Flower", cursive;
    color: var(--tagline);
    white-space: nowrap;
    line-height: 1;
  }
  .card--front .tagline {
    left: 292px;
    top: 198px;
    font-size: 25px;
  }

  /* Back */
  .contact {
    position: absolute;
    right: 36px;
    top: 54px;
    text-align: right;
    color: var(--white);
    font-family: "Nunito", sans-serif;
  }
  .contact__name {
    font-family: "Indie Flower", cursive;
    font-weight: 400;
    color: var(--sunshine);
    font-size: 42px;
    line-height: 1;
  }
  .contact__role {
    font-size: 16px;
    margin-top: 4px;
  }
  .contact__details {
    list-style: none;
    margin-top: 26px;
    font-size: 19px;
    line-height: 1.18;
  }
  .card--back .brand-name {
    left: 40px;
    top: 286px;
    font-size: 28px;
  }
  .card--back .tagline {
    left: 40px;
    top: 320px;
    font-size: 17px;
  }
</style>
</head>
<body>
<main class="canvas">

  <section class="card card--front" aria-label="Business card front">
    <svg class="card__bg" viewBox="0 0 620 378" preserveAspectRatio="none" aria-hidden="true">
      <path d="M0,0 H128 C78,120 78,270 210,378 H0 Z" fill="var(--slate)"/>
      <path d="M134,0 C84,120 84,270 220,378" fill="none" stroke="var(--slate-light)" stroke-width="9"/>
    </svg>
    <span class="brand-mark" aria-hidden="true"></span>
    <h1 class="brand-name">Bright Dabs</h1>
    <p class="tagline">Face Painting Designs</p>
  </section>

  <section class="card card--back" aria-label="Business card back">
    <svg class="card__bg" viewBox="0 0 620 378" preserveAspectRatio="none" aria-hidden="true">
      <path d="M0,200 C150,210 300,300 450,300 C530,300 590,270 620,262 V378 H0 Z" fill="var(--slate-light)"/>
      <path d="M0,212 C150,222 300,314 450,314 C530,314 590,284 620,276 V378 H0 Z" fill="var(--sunshine)"/>
    </svg>
    <div class="contact">
      <h2 class="contact__name">maren lockwell</h2>
      <p class="contact__role">Artist</p>
      <ul class="contact__details">
        <li>0491 283 516</li>
        <li>maren@brightdabs.com.au</li>
        <li>www.brightdabs.com.au</li>
      </ul>
    </div>
    <p class="brand-name">Bright Dabs</p>
    <p class="tagline">Face Painting Designs</p>
  </section>

</main>
</body>
</html>
```